Sports Field sign

Our business provides audio visual solutions to corporate and government clients. We have purchased space at a sports field to place two signs to promote our business. We need to provide the artwork in high res format for a sign to be placed at a sports oval. The physical sign will be 900mm high and 7000mm long. It needs to include our logo, contact number, and the services we offer. It needs to be tidy, easy to read and easily visible from a distance. The sample I have done is very basic but covers what we need - I would expect that a designer can produce an eye-catching impressive sign with this much space to work with., and may even include some flashy background, an image or creative design to get attention.

examples of what signs are up at the oval now here - https://chirpline.example/GRL/status/4820913375561029417?s=31&t=8-qLmR3kdopyTUwZcQ_xP

Our Company web site is www.brightmesh.example.au

```html
<!DOCTYPE html>
<html lang="en">
<head>
<meta charset="utf-8">
<title>Brightmesh AV – Sports Field Sign</title>
<link rel="stylesheet" href="https://fonts.googleapis.com/css2?family=Montserrat:wght@500;600;800&family=Open+Sans:wght@400&display=swap">
<style>
  :root {
    --backdrop: #8e8e8e;
    --panel-dark: #1b1b1b;
    --brand-blue: #3a55a4;
    --brand-sky: #8ab8e6;
    --brand-orange: #e8612a;
    --paper: #ffffff;
    --ink: #111111;
  }
  html, body {
    margin: 0;
    padding: 0;
    width: 1200px;
    height: 504px;
    overflow: hidden;
    background: var(--backdrop);
  }
  .canvas {
    position: relative;
    width: 1200px;
    height: 504px;
    overflow: hidden;
    font-family: "Montserrat", sans-serif;
  }
  .sign {
    position: absolute;
    left: 55px;
    top: 181px;
    width: 1091px;
    height: 141px;
    background: var(--paper);
  }
  .sign-shapes {
    position: absolute;
    inset: 0;
    width: 100%;
    height: 100%;
  }
  .txt {
    position: absolute;
    margin: 0;
    line-height: 1;
    white-space: nowrap;
  }
  .brand-mark {
    position: absolute;
    left: 37px;
    top: 28px;
    width: 36px;
    height: 36px;
    background: var(--brand-blue);
  }
  .brand-name {
    left: 85px;
    top: 28px;
    font-family: "Open Sans", sans-serif;
    font-weight: 400;
    font-size: 30px;
    color: var(--paper);
  }
  .tagline {
    left: 37px;
    top: 76px;
    font-weight: 500;
    font-size: 11px;
    letter-spacing: 0.6px;
    color: var(--paper);
  }
  .capabilities {
    left: 37px;
    top: 105px;
    font-weight: 500;
    font-size: 14px;
    letter-spacing: 0.3px;
    color: var(--brand-sky);
  }
  .service {
    font-weight: 500;
    font-size: 21px;
    color: var(--ink);
    letter-spacing: 0.2px;
  }
  .service::before {
    content: "";
    position: absolute;
    left: -28px;
    top: 2px;
    width: 16px;
    height: 16px;
    background: var(--brand-blue);
  }
  .svc-video { left: 525px; top: 23px; }
  .svc-signage { left: 518px; top: 54px; }
  .svc-led { left: 845px; top: 24px; }
  .svc-audio { left: 836px; top: 53px; }
  .phone-number {
    left: 499px;
    top: 102px;
    font-weight: 800;
    font-size: 34px;
    color: var(--paper);
    letter-spacing: 0.5px;
  }
  .city {
    font-weight: 600;
    font-size: 12.5px;
    color: var(--paper);
    letter-spacing: 0.3px;
  }
  .city-melbourne { left: 850px; top: 99px; }
  .city-sydney { left: 850px; top: 117px; }
  .city-brisbane { left: 967px; top: 99px; }
  .city-perth { left: 967px; top: 117px; }
</style>
</head>
<body>
<div class="canvas">
  <div class="sign">
    <svg class="sign-shapes" viewBox="0 0 1091 141" preserveAspectRatio="none" aria-hidden="true">
      <polygon points="0,0 469,0 418,141 0,141" fill="#1b1b1b"/>
      <polygon points="469,0 482,0 438,96 434,96" fill="#8ab8e6"/>
      <polygon points="438,96 780,96 759,141 418,141" fill="#3a55a4"/>
      <polygon points="780,86 1091,86 1091,141 759,141" fill="#e8612a"/>
      <circle cx="475" cy="117" r="15" fill="#ffffff"/>
      <path d="M469,109 l3,-1 l3,5 l-2,2 q2,4 6,6 l2,-2 l5,3 l-1,3 q-2,2 -5,1 q-9,-4 -12,-12 q-1,-3 1,-5 z" fill="#3a55a4"/>
      <path d="M798,107 a8.5,8.5 0 1 1 17,0 q0,7 -8.5,16 q-8.5,-9 -8.5,-16 z" fill="#ffffff"/>
      <circle cx="806.5" cy="107" r="3.2" fill="#e8612a"/>
      <ellipse cx="806.5" cy="126" rx="16" ry="4.5" fill="none" stroke="#ffffff" stroke-width="2"/>
      <g fill="none" stroke="#ffffff" stroke-width="2.6" stroke-linecap="round" stroke-linejoin="round">
        <polyline points="835,106 839,110 846,102"/>
        <polyline points="835,124 839,128 846,120"/>
        <polyline points="952,106 956,110 963,102"/>
        <polyline points="952,124 956,128 963,120"/>
      </g>
    </svg>

    <div class="brand-mark"></div>
    <p class="txt brand-name">brightmesh av</p>
    <p class="txt tagline">SOUND AND SCREENS FOR EVERY ROOM</p>
    <p class="txt capabilities">DESIGN | CONSULTING | SERVICE | MAINTENANCE</p>

    <p class="txt service svc-video">VIDEO CONFERENCING</p>
    <p class="txt service svc-signage">DIGITAL SIGNAGE</p>
    <p class="txt service svc-led">L.E.D VIDEO WALLS</p>
    <p class="txt service svc-audio">AUDIO SOLUTIONS</p>

    <p class="txt phone-number">1300 555 017</p>

    <p class="txt city city-melbourne">MELBOURNE</p>
    <p class="txt city city-sydney">SYDNEY</p>
    <p class="txt city city-brisbane">BRISBANE</p>
    <p class="txt city city-perth">PERTH</p>
  </div>
</div>
</body>
</html>
```